PowerPoint Template - Orvik Point

You find in the attached file a short description of our firm, logo, mission, vision and values. We made an empty template in order to let you free to imagine. We-have high expectations on ideas "out of the box" to merge our job (consulting firm) with Zen concept. We really Would like "Zen" look and feel, to show our difference. And we want to avoid "standard consulting" (smart guys with ties, shaking hand with Pellam smilies ...) Thank you

Target Market(s)

organization (Rather big ones)

Industry/Entity Type

Consulting

Number of Pages Required

3 page

Font styles to use
Sans Serif

Requirements
Must have
• - Some nice pictures - Be really "Zen" (quiet, smart, luxury, people centric)
Should not have
• really looks like "standard consulting" (smart guys with ties, shaking hand with Pellam smilies ...)

```html
<!DOCTYPE html>
<html lang="en">
<head>
<meta charset="utf-8">
<title>Orvik Point – Presentation Template</title>
<link rel="stylesheet" href="https://fonts.googleapis.com/css2?family=Ubuntu:ital,wght@0,300;0,400;0,500;1,400&display=swap">
<style>
  :root {
    --orange: #ee7a3f;
    --green: #8cc68d;
    --green-soft: #a9d3a6;
    --grey: #8b8b8d;
    --grey-text: #7a7a7c;
    --white: #ffffff;
    --cream: #f6efe6;
    --stage: #e4e4e4;
  }
  html, body { margin: 0; padding: 0; overflow: hidden; }
  body { width: 1200px; height: 1000px; background: var(--stage); font-family: "Ubuntu", sans-serif; position: relative; }
  .slide { position: absolute; width: 367px; height: 206px; background: var(--white); overflow: hidden; }
  .slide > * { position: absolute; }
  .photo { }
  .brand-tag { right: 10px; top: 8px; font-size: 8px; font-weight: 500; color: var(--orange); display: flex; align-items: center; gap: 3px; }
  .brand-tag::before { content: ""; width: 9px; height: 9px; border: 1.5px solid currentColor; border-radius: 50%; }
  .brand-tag.green { color: var(--green); }
  .title { font-size: 17px; font-weight: 400; text-transform: uppercase; letter-spacing: .2px; margin: 0; }
  .cloud-title { font-size: 16px; margin: 0; }
  .cloud-title em { font-style: italic; }
  .tag-list { list-style: none; margin: 0; padding: 0; font-size: 14px; font-weight: 300; color: var(--grey-text); line-height: 16px; }
  .tag-list li::before { content: "• "; color: var(--green); }
  .tag-list.orange-dots li::before { color: var(--orange); }
  .word-box { width: 112px; height: 110px; padding: 10px 10px; box-sizing: border-box; color: var(--white); }
  .word-box h3 { margin: 0 0 8px; font-size: 18px; font-weight: 400; }
  .word-box ul { margin: 0; padding: 0; list-style: none; font-size: 9.5px; line-height: 11.5px; }
  .word-box li::before { content: "• "; }
  .paradox { width: 60px; text-align: center; font-size: 5.5px; color: var(--grey-text); }
  .paradox svg { display: block; margin: 0 auto 4px; }
  .paradox.on-grey { color: var(--white); }
</style>
</head>
<body>

<!-- Cover -->
<section class="slide cover" style="left:218px;top:42px;">
  <div class="photo" role="img" aria-label="Faint photo of a desk with a vintage toy car" style="inset:0;background:linear-gradient(180deg,#e9e6e2,#f3f1ee);"></div>
  <div style="left:0;top:0;width:271px;height:54px;background:var(--orange);opacity:.75;"></div>
  <div style="left:271px;top:0;width:96px;height:54px;background:var(--green);opacity:.7;"></div>
  <div style="left:0;top:54px;width:367px;height:100px;background:rgba(255,255,255,.88);"></div>
  <div style="left:0;top:154px;width:233px;height:52px;background:var(--green);opacity:.7;"></div>
  <div style="left:233px;top:154px;width:134px;height:52px;background:var(--grey);opacity:.8;"></div>
  <div class="cover-name" style="left:0;width:367px;top:92px;text-align:center;font-size:22px;font-weight:400;letter-spacing:4px;color:var(--orange);">ORVIK POINT</div>
  <div style="left:176px;top:70px;width:14px;height:14px;border:2px solid var(--orange);border-radius:50%;"></div>
</section>

<!-- Activity & Contest / convictions -->
<section class="slide" style="left:615px;top:42px;">
  <div class="photo" role="img" aria-label="Photo of a person in a blue shirt holding colourful paint brushes" style="left:27px;top:10px;width:268px;height:188px;background:linear-gradient(135deg,#c9d6e6,#8fa9c9 55%,#e9c9a6);opacity:.9;"></div>
  <span class="brand-tag">Orvik Point</span>
  <h2 class="title" style="left:15px;top:25px;color:var(--orange);">Activity &amp; Contest</h2>
  <div style="left:12px;top:103px;width:209px;height:87px;background:var(--grey);opacity:.95;"></div>
  <p style="left:22px;top:121px;width:195px;margin:0;color:var(--white);font-size:14px;line-height:19px;"><span style="color:var(--orange);">Orvik Point</span> is a management, organization and performance improvement consulting firm.</p>
  <svg style="left:247px;top:24px;" width="102" height="174" viewBox="0 0 102 174"><path d="M0 0H102V162H30L22 174L16 162H0Z" fill="#8cc68d" opacity=".9"/></svg>
  <div style="left:252px;top:40px;width:92px;text-align:right;color:var(--grey-text);font-size:13px;line-height:13px;">Our<br>convictions</div>
  <p style="left:252px;top:79px;width:92px;margin:0;text-align:right;color:var(--white);font-size:6.3px;line-height:9.3px;"><span style="font-size:11px;">In</span> a hyper competitive environment only organizations able to quickly adapt will survive. Digital companies will have a competitive advantage because they will understand their ecosystem better, faster and will act more effectively than others.</p>
</section>

<!-- Mission -->
<section class="slide" style="left:218px;top:279px;">
  <div class="photo" role="img" aria-label="Photo of a bright loft room with a window and a stool" style="left:195px;top:0;width:172px;height:206px;background:linear-gradient(180deg,#f2f2f0,#dcd9d4 60%,#bdb7ae);"></div>
  <div style="left:0;top:0;width:195px;height:206px;background:var(--grey);"></div>
  <span class="brand-tag">Orvik Point</span>
  <h2 class="title" style="left:15px;top:22px;color:var(--white);">Activity &amp; Contest</h2>
  <div style="left:24px;top:65px;font-size:14px;color:var(--green-soft);">Our Mission</div>
  <div style="left:24px;top:84px;width:170px;font-size:6.5px;color:var(--white);">is to support the digital transformation of our clients.</div>
  <div style="left:24px;top:101px;font-size:14px;color:var(--green-soft);">Our differences</div>
  <div style="left:10px;top:124px;width:170px;font-size:6.5px;line-height:9px;color:var(--white);">
    <p style="margin:0 0 6px;padding-left:14px;position:relative;"><span style="position:absolute;left:0;color:var(--orange);">›</span>Use Lean and Agile known methods in innovative ways, creating quickly measurable value.</p>
    <p style="margin:0;padding-left:14px;position:relative;"><span style="position:absolute;left:0;color:var(--orange);">›</span>Avoid stress and permanent emergency, accept mistakes to bounce back quickly.</p>
  </div>
</section>

<!-- Name explanation -->
<section class="slide" style="left:615px;top:279px;">
  <div class="photo" role="img" aria-label="Photo of a living room with a patterned rug and a small plant" style="left:0;top:92px;width:367px;height:114px;background:linear-gradient(180deg,#ecebe8,#d8cbbd 70%,#c47a5e);opacity:.85;"></div>
  <span class="brand-tag">Orvik Point</span>
  <h2 class="title" style="left:15px;top:22px;color:var(--grey-text);">Name Explanation</h2>
  <div class="word-box" style="left:57px;top:68px;background:var(--green-soft);">
    <h3 style="color:var(--orange);">Orvik</h3>
    <ul><li>No stress</li><li>Respect</li><li>Human centric</li><li>Accept mistakes</li></ul>
  </div>
  <div class="word-box" style="left:209px;top:68px;background:var(--grey);">
    <h3 style="color:var(--green-soft);">Point</h3>
    <ul><li>Value for customers and for ourselves</li><li>Value by action</li><li>Quick Value</li><li>Measurable value</li></ul>
  </div>
</section>

<!-- Paradoxes -->
<section class="slide" style="left:218px;top:515px;">
  <div class="photo" role="img" aria-label="Faint photo of a desk with a laptop and a water bottle" style="left:0;top:0;width:184px;height:206px;background:linear-gradient(180deg,#f8f8f7,#ececea);"></div>
  <div style="left:184px;top:0;width:183px;height:206px;background:var(--grey);"></div>
  <span class="brand-tag green">Orvik Point</span>
  <h2 class="title" style="left:85px;top:23px;color:var(--orange);">Paradoxes <span style="color:var(--green-soft);">we defend</span></h2>
  <div class="paradox" style="left:7px;top:68px;"><svg width="40" height="40" viewBox="0 0 40 40"><circle cx="20" cy="20" r="18" fill="none" stroke="#8b8b8d" stroke-width="2"/><rect x="12" y="13" width="16" height="11" fill="none" stroke="#ee7a3f" stroke-width="1.8"/><path d="M17 28h6M20 24v4" stroke="#ee7a3f" stroke-width="1.8"/></svg>Zen and Digital</div>
  <div class="paradox" style="left:45px;top:95px;"><svg width="40" height="40" viewBox="0 0 40 40"><circle cx="20" cy="20" r="18" fill="none" stroke="#8b8b8d" stroke-width="2"/><path d="M22 10l-7 11h5l-2 9 7-12h-5z" fill="none" stroke="#ee7a3f" stroke-width="1.8"/></svg>Zen and Quick</div>
  <div class="paradox" style="left:123px;top:122px;"><svg width="42" height="42" viewBox="0 0 40 40"><circle cx="20" cy="20" r="18" fill="none" stroke="#8b8b8d" stroke-width="2"/><path d="M27 20a7 7 0 1 1-3-6" fill="none" stroke="#ee7a3f" stroke-width="1.8"/><path d="M24 10v5h5" fill="none" stroke="#ee7a3f" stroke-width="1.8"/></svg>Zen and Action</div>
  <div class="paradox on-grey" style="left:182px;top:121px;"><svg width="42" height="42" viewBox="0 0 40 40"><circle cx="20" cy="20" r="18" fill="none" stroke="#fff" stroke-width="2"/><path d="M10 25l15-15 5 5-15 15z M15 20l2 2M18 17l2 2M21 14l2 2" fill="none" stroke="#8cc68d" stroke-width="1.6"/></svg>Value and Measurable</div>
  <div class="paradox on-grey" style="left:240px;top:92px;"><svg width="42" height="42" viewBox="0 0 40 40"><circle cx="20" cy="20" r="18" fill="none" stroke="#fff" stroke-width="2"/><path d="M11 25a9 9 0 1 1 18 0" fill="none" stroke="#8cc68d" stroke-width="1.8"/><path d="M20 25l4-7" stroke="#8cc68d" stroke-width="1.8"/></svg>Value and Quick</div>
  <div class="paradox on-grey" style="left:296px;top:69px;"><svg width="42" height="42" viewBox="0 0 40 40"><circle cx="20" cy="20" r="18" fill="none" stroke="#fff" stroke-width="2"/><circle cx="15" cy="16" r="3" fill="none" stroke="#8cc68d" stroke-width="1.6"/><circle cx="25" cy="16" r="3" fill="none" stroke="#8cc68d" stroke-width="1.6"/><path d="M10 27c0-4 2-6 5-6s5 2 5 6M20 27c0-4 2-6 5-6s5 2 5 6" fill="none" stroke="#8cc68d" stroke-width="1.6"/></svg>Customers and Employees, both first</div>
</section>

<!-- Cloud tag People -->
<section class="slide" style="left:615px;top:515px;">
  <div class="photo" role="img" aria-label="Photo of a wooden desk with a laptop and headphones in a bright office" style="inset:0;background:linear-gradient(160deg,#f1efec,#d9c3a5 60%,#b98c5f);"></div>
  <div style="left:172px;top:0;width:195px;height:206px;background:rgba(255,255,255,.78);"></div>
  <span class="brand-tag green">Orvik Point</span>
  <h2 class="cloud-title" style="left:178px;top:24px;color:var(--orange);font-weight:400;">CLOUD TAG - <em>People</em></h2>
  <ul class="tag-list" style="left:243px;top:73px;"><li>Serenity</li><li>Zen</li><li>Respect</li><li>Trust</li><li>Open</li></ul>
</section>

<!-- Cloud tag Action -->
<section class="slide" style="left:218px;top:752px;">
  <div class="photo" role="img" aria-label="Photo of an orange chair at a wooden desk on a parquet floor" style="inset:0;background:linear-gradient(150deg,#e8e3dc,#c9955f 55%,#b27a45);"></div>
  <div style="left:172px;top:0;width:195px;height:206px;background:rgba(250,243,233,.9);"></div>
  <span class="brand-tag">Orvik Point</span>
  <h2 class="cloud-title" style="left:178px;top:24px;color:var(--green);font-weight:400;">CLOUD TAG - <em>Action</em></h2>
  <ul class="tag-list orange-dots" style="left:197px;top:73px;"><li>Pragmatism</li><li>Quick</li><li>Commitment</li><li>Measurable</li><li>Customer value oriented</li><li>Meaningful</li></ul>
</section>

<!-- Cloud tag Vision -->
<section class="slide" style="left:615px;top:752px;">
  <div class="photo" role="img" aria-label="Photo of a laptop on a wooden table with potted plants" style="inset:0;background:linear-gradient(160deg,#ebe7e1,#a9865f 60%,#7a6048);"></div>
  <div style="left:172px;top:0;width:195px;height:206px;background:rgba(255,255,255,.85);"></div>
  <span class="brand-tag green">Orvik Point</span>
  <h2 class="cloud-title" style="left:178px;top:24px;color:var(--orange);font-weight:400;">CLOUD TAG - <em>Vision</em></h2>
  <ul class="tag-list" style="left:197px;top:70px;font-size:17px;line-height:20px;"><li>360°</li><li>Early</li></ul>
</section>

</body>
</html>
```